Zielgruppe
BVRT ist ein Beratungsunternehmen im Bereich Information- und Content-Management. Wir unterstützen bei der Auswahl, Einführung und Betreuung unterschiedlichster Systemlösungen. Unser Ziel ist es, Informationsflüsse reibungslos zu gestalten, indem wir gemeinsam mit unseren Kunden ihre Informationslandschaft analysieren und optimieren. Dabei bringen wir Know-how zu Tools, Methoden und Strategien ein.
Aufgabenstellung

```html
<!DOCTYPE html>
<html lang="de">
<head>
<meta charset="utf-8">
<title>BVRT – Information- &amp; Content-Management</title>
<link href="https://fonts.googleapis.com/css2?family=Arimo:wght@400;700&display=swap" rel="stylesheet">
<style>
  :root {
    --green: #9bc23c;
    --blue: #1d8fd8;
    --ink: #333;
    --white: #fff;
    --bg: #ededed;
    --partner-grey: #c9ced3;
  }
  * { box-sizing: border-box; margin: 0; padding: 0; }
  html, body { width: 1200px; height: 639px; overflow: hidden; }
  body { font-family: "Arimo", Arial, sans-serif; background: var(--bg); }
  .canvas {
    position: relative; width: 1200px; height: 639px; overflow: hidden;
    background: linear-gradient(180deg, #efefef 0%, #f4f4f4 45%, #e9ece4 100%);
  }
  .top-band { position: absolute; left: 0; top: 0; width: 100%; height: 96px; background: var(--white); }
  .pattern-field {
    position: absolute; left: 0; top: 400px; width: 100%; height: 239px;
    background:
      radial-gradient(ellipse 40% 30% at 20% 55%, rgba(155,194,60,.35), transparent 70%),
      radial-gradient(ellipse 35% 30% at 75% 70%, rgba(155,194,60,.3), transparent 70%),
      linear-gradient(180deg, rgba(220,222,222,0) 0%, rgba(205,208,205,.7) 60%, rgba(225,228,222,.9) 100%);
  }
  .divider { position: absolute; left: 471px; top: 0; width: 2px; height: 639px; background: var(--blue); }

  .brand-name {
    position: absolute; left: 86px; top: 32px;
    font-size: 40px; line-height: 44px; font-weight: 400; color: var(--green);
  }

  .cooperation {
    position: absolute; right: 40px; top: 64px;
    display: flex; align-items: baseline; gap: 10px;
    font-size: 13px; color: var(--ink);
  }
  .partner-brand-name { font-size: 16px; font-weight: 400; color: var(--ink); }

  .card {
    position: absolute; background: var(--white); border-radius: 30px;
    box-shadow: 0 4px 14px rgba(0,0,0,.18);
  }
  .card-intro { left: 52px; top: 155px; width: 378px; height: 317px; }
  .intro-title {
    position: absolute; left: 29px; top: 26px;
    font-size: 41px; line-height: 51px; font-weight: 700; color: var(--green);
  }
  .partners-label { position: absolute; left: 35px; top: 200px; font-size: 13px; color: var(--ink); }
  .partner-grid {
    position: absolute; left: 27px; top: 226px; width: 335px;
    display: grid; grid-template-columns: repeat(4, 1fr); gap: 14px 10px;
  }
  .partner-badge { height: 24px; border-radius: 4px; background: var(--partner-grey); }

  .card-services { left: 591px; top: 155px; width: 392px; height: 396px; }
  .services-banner {
    position: absolute; left: 0; top: 36px; width: 392px; height: 102px;
    background: var(--green); color: var(--white);
    font-size: 30px; line-height: 37px; font-weight: 700; padding: 17px 0 0 20px;
  }
  .service-list { position: absolute; left: 28px; top: 154px; list-style: none; }
  .service-list li {
    position: relative; padding-left: 14px; margin-bottom: 14px;
    font-size: 20px; line-height: 24px; font-weight: 700; color: var(--green);
  }
  .service-list li::before { content: "·"; position: absolute; left: 0; top: 0; }
</style>
</head>
<body>
<main class="canvas">
  <div class="top-band"></div>
  <div class="pattern-field" role="img" aria-label="Dekoratives Muster aus grünen und grauen abgerundeten Balken"></div>
  <div class="divider"></div>

  <p class="brand-name">BVRT</p>

  <p class="cooperation">in Zusammenarbeit mit: <span class="partner-brand-name">Verbundo</span></p>

  <section class="card card-intro">
    <h1 class="intro-title">Information- &amp;<br>Content-<br>Management</h1>
    <p class="partners-label">Unsere Partner</p>
    <div class="partner-grid">
      <span class="partner-badge"></span><span class="partner-badge"></span>
      <span class="partner-badge"></span><span class="partner-badge"></span>
      <span class="partner-badge"></span><span class="partner-badge"></span>
      <span class="partner-badge"></span><span class="partner-badge"></span>
    </div>
  </section>

  <section class="card card-services">
    <h2 class="services-banner">Unabhängige Beratung,<br>individuelle Lösungen</h2>
    <ul class="service-list">
      <li>Knowledge Graph</li>
      <li>Digital Information Twin</li>
      <li>Systemoptimierung &amp; -Auto-<br>matisierung</li>
      <li>Agiles Projektmanagement</li>
      <li>Business Data Analytics</li>
    </ul>
  </section>
</main>
</body>
</html>
```